資格は全部で2種類あります。
各々コースが2つに分かれており、それぞれ初級・中級・上級があります。
コース・級ごとに色合いを変えていただければと思っております。
※デザイン2種:各6色(2つのコース×3つの級)の色合い変更

今回はコンペ形式にて1種類のデザインを募集させていただきます。
採用させていただいた方には、2種類ともデザインしていただければと思っております。

また、認定証のデザインをもとにした、認定カードのデザインもお願いいたします。
※認定証同様、デザイン2種各6色の色合い変更

採用報酬は、認定証・認定カードのすべてのデザインを含めた金額になります。
今回のコンペでは、下記2点の認定証のデザインを募集させていただきます。
①「創造育成指導員」という資格の「発達障がい支援コース」の「初級」
②「デジタル匠指導員」という資格の「IT実践コース」の「初級」

記載いただきたい項目は下記の通りになります。

・初級
・認定証
・発達障がい支援アドバイザー
・●●殿
・●●年●月●日
・あなたは当カリキュラムを修了されましたので、『初級・発達障がい支援アドバイザー』として認定いたします。
・NPO法人青葉学習推進会

・初級
・認定証
・IT実践アシスタント
・●●殿
・●●年●月●日
・あなたは当カリキュラムを修了されましたので、『初級・IT実践アシスタント』として認定いたします。
・NPO法人青葉学習推進会
認定証はカミノハコにて発注予定となっているため、イラストレーターのデータにて納品いただきますようお願いいたします。
テンプレートにつきましては、下記ギガファイル便のデータをご確認ください。
https://files.examplestore-transfer.jp/1008-a71c2e9b40f35d8862e1c7a04b5f2913e

また、ロゴや認定証のサンプルを添付させていただきます。
イラストレーターのデータにつきましては下記ギガファイル便をご確認ください。
https://files.examplestore-transfer.jp/1005-3b8e0f41c92d7a65e0b1f4d82c6a07e15

ゴールドを差し色とした素敵なデザインであったので選ばせていただきました。
ありがとうございました。

この度は弊社のコンペにご参加いただきありがとうございました。
また機会がございましたら、よろしくお願いいたします。

```html
<!DOCTYPE html>
<html lang="ja">
<head>
<meta charset="UTF-8">
<title>認定証 初級 発達障がい支援アドバイザー</title>
<link href="https://fonts.googleapis.com/css2?family=Noto+Serif+JP:wght@400;600;700;900&display=swap" rel="stylesheet">
<style>
  :root {
    --pink-light: #f6d9e6;
    --pink: #e9b3cc;
    --pink-deep: #d48fb0;
    --frame-brown: #6b3a2a;
    --gold-light: #f3dfa0;
    --gold: #c9a24a;
    --gold-deep: #9a7426;
    --ink: #1f1a18;
    --card: #ffffff;
    --badge-navy: #1d3f8a;
    --badge-blue: #3f6fc4;
  }
  * { margin: 0; padding: 0; box-sizing: border-box; }
  html, body { width: 849px; height: 1200px; overflow: hidden; background: #ffffff; }
  .certificate {
    position: relative;
    width: 849px;
    height: 1200px;
    overflow: hidden;
    font-family: "Noto Serif JP", serif;
    color: var(--ink);
    background: radial-gradient(ellipse at 50% 40%, var(--pink-light) 0%, var(--pink) 65%, var(--pink-deep) 100%);
  }
  .frame-line {
    position: absolute;
    inset: 14px;
    border: 4px solid var(--frame-brown);
    box-shadow: inset 0 0 0 3px var(--gold-light);
  }
  .vine {
    position: absolute;
    opacity: 0.45;
  }
  .vine--top-left {
    left: 18px; top: 18px; width: 260px; height: 620px;
    background: radial-gradient(ellipse at 20% 35%, var(--gold) 0%, rgba(201,162,74,0.25) 40%, rgba(201,162,74,0) 70%);
  }
  .vine--bottom-right {
    right: 18px; bottom: 18px; width: 280px; height: 520px;
    background: radial-gradient(ellipse at 80% 65%, var(--gold) 0%, rgba(201,162,74,0.25) 40%, rgba(201,162,74,0) 70%);
  }
  .card-shape { position: absolute; left: 0; top: 0; }
  .badge { position: absolute; left: 660px; top: 10px; width: 160px; height: 160px; }
  .heading {
    position: absolute;
    top: 292px; left: 0; width: 849px;
    text-align: center;
  }
  .heading__label {
    display: inline-block;
    font-size: 20px;
    font-weight: 600;
    letter-spacing: 0.5em;
    padding: 4px 30px 4px 40px;
    border-top: 2px solid var(--gold);
    border-bottom: 2px solid var(--gold);
  }
  .heading__title {
    margin-top: 22px;
    font-size: 70px;
    font-weight: 900;
    line-height: 1.42;
    letter-spacing: 0.03em;
  }
  .recipient {
    position: absolute;
    left: 113px; top: 628px;
    width: 580px; height: 42px;
    border-bottom: 1.5px solid var(--ink);
    text-align: right;
    font-size: 20px;
    font-weight: 600;
    padding-right: 18px;
  }
  .issue-date {
    position: absolute;
    left: 180px; top: 708px;
    width: 410px;
    display: flex;
    justify-content: space-between;
    font-size: 15px;
    font-weight: 600;
  }
  .statement {
    position: absolute;
    top: 832px; left: 0; width: 849px;
    text-align: center;
    font-size: 16px;
    font-weight: 600;
    line-height: 2.9;
  }
  .issuer {
    position: absolute;
    top: 975px; left: 0; width: 849px;
    display: flex;
    justify-content: center;
    align-items: center;
    gap: 12px;
    font-size: 22px;
    font-weight: 700;
    color: var(--frame-brown);
  }
  .issuer__mark {
    width: 18px; height: 18px;
    border-radius: 50%;
    background: var(--frame-brown);
  }
</style>
</head>
<body>
<main class="certificate">
  <div class="vine vine--top-left" role="img" aria-label="金色のつる草の飾り"></div>
  <div class="vine vine--bottom-right" role="img" aria-label="金色のつる草の飾り"></div>
  <div class="frame-line"></div>

  <svg class="card-shape" width="849" height="1200" viewBox="0 0 849 1200" aria-hidden="true">
    <defs>
      <linearGradient id="goldSweep" x1="0" y1="0" x2="1" y2="0">
        <stop offset="0" stop-color="#9a7426"/>
        <stop offset="0.35" stop-color="#f3dfa0"/>
        <stop offset="0.65" stop-color="#c9a24a"/>
        <stop offset="1" stop-color="#f6e6b4"/>
      </linearGradient>
    </defs>
    <path d="M62 240 Q380 215 560 150 Q690 100 787 22 L787 1040 Q420 1060 62 1095 Z" fill="var(--card)"/>
    <path d="M62 240 Q380 215 560 150 Q690 100 787 22" fill="none" stroke="url(#goldSweep)" stroke-width="7"/>
    <path d="M40 228 Q360 200 540 136 Q660 92 740 30" fill="none" stroke="url(#goldSweep)" stroke-width="3"/>
    <path d="M62 1095 Q420 1060 787 1040" fill="none" stroke="url(#goldSweep)" stroke-width="7"/>
    <path d="M40 1110 Q420 1072 810 1052" fill="none" stroke="url(#goldSweep)" stroke-width="3"/>
  </svg>

  <svg class="badge" viewBox="0 0 150 150" aria-label="初級">
    <circle cx="75" cy="75" r="72" fill="var(--gold)"/>
    <circle cx="75" cy="75" r="64" fill="var(--badge-navy)"/>
    <circle cx="75" cy="75" r="58" fill="none" stroke="var(--gold-light)" stroke-width="2"/>
    <path d="M5 72 H145 V104 H5 Z" fill="var(--badge-blue)"/>
    <g fill="var(--gold-light)">
      <path d="M50 48 l3 7 7 0 -5.5 4.5 2 7 -6.5 -4 -6.5 4 2 -7 -5.5 -4.5 7 0z"/>
      <path d="M75 40 l3 7 7 0 -5.5 4.5 2 7 -6.5 -4 -6.5 4 2 -7 -5.5 -4.5 7 0z"/>
      <path d="M100 48 l3 7 7 0 -5.5 4.5 2 7 -6.5 -4 -6.5 4 2 -7 -5.5 -4.5 7 0z"/>
    </g>
    <text x="75" y="99" text-anchor="middle" font-family="Noto Serif JP, serif" font-size="28" font-weight="900" fill="#ffffff">初級</text>
  </svg>

  <header class="heading">
    <div class="heading__label">認定証</div>
    <h1 class="heading__title">発達障がい<br>支援アドバイザー</h1>
  </header>

  <div class="recipient">殿</div>

  <div class="issue-date"><span>令和</span><span>年</span><span>月</span><span>日</span></div>

  <p class="statement">あなたは当カリキュラムを修了されましたので、<br>「初級・発達障がい支援アドバイザー」として認定いたします。</p>

  <footer class="issuer"><span class="issuer__mark"></span><span>NPO法人青葉学習推進会</span></footer>
</main>
</body>
</html>
```